Halvorine Ledgers & Advisory Tri-Fold Brochure (8.5"x11")

I need a professional looking brochure for my bookkeeping business. I am looking for something professional yet casual (not too corporate looking). I have attached a sample brochure that will outline the areas and a copy of our logo. I'd like to stick with shades of blue. The final product should communicate professional and personal.

Target Market(s)

Small service businesses.

Industry/Entity Type

Business

Font styles to use
Sans Serif

Requirements
Must have
• Professional looking photos of people in areas where it asks for a picture.

```html
<!DOCTYPE html>
<html lang="en">
<head>
<meta charset="utf-8">
<title>Halvorine Ledgers &amp; Advisory – Tri-Fold Brochure</title>
<link rel="stylesheet" href="https://fonts.googleapis.com/css2?family=Open+Sans:wght@400;600;700&family=Tinos:wght@400;700&display=swap">
<style>
  :root {
    --blue: #1f8fd8;
    --blue-bright: #35a9ec;
    --blue-deep: #136aa8;
    --ink: #262729;
    --ink-deep: #1b1c1e;
    --paper: #ffffff;
    --mist: #eceff2;
    --grey-text: #555b61;
    --stage: #e4e6e8;
    --head: "Tinos", "Times New Roman", serif;
    --body: "Open Sans", Arial, sans-serif;
  }
  * { box-sizing: border-box; margin: 0; padding: 0; }
  html, body { width: 696px; height: 1200px; overflow: hidden; }
  body { background: var(--stage); font-family: var(--body); position: relative; }

  .brochure {
    position: absolute; left: 32px; width: 632px; height: 490px;
    overflow: hidden; box-shadow: 0 2px 8px rgba(0,0,0,.25);
  }
  .brochure--outside { top: 50px; background: var(--mist); }
  .brochure--inside { top: 660px; background: var(--paper); }
  .brochure > * { position: absolute; }
  .panel-art { left: 0; top: 0; width: 632px; height: 490px; }

  .photo { display: block; }
  .photo--desk { left: 0; top: 220px; width: 211px; height: 260px;
    background: linear-gradient(160deg, #f1f5f9 0%, #c9dbea 45%, #6f9cc4 100%); }
  .photo--team { left: 422px; top: 105px; width: 210px; height: 260px;
    background: radial-gradient(ellipse at 45% 50%, #d9dde3 0%, #9aa6b3 55%, #4a5563 100%); }
  .photo--growth { left: 211px; top: 0; width: 421px; height: 230px;
    background: linear-gradient(100deg, #dfe6ee 0%, #8aa0b8 35%, #2c3b52 65%, #c97a2c 88%, #2b3446 100%); }
  .photo--coins { left: 0; top: 290px; width: 211px; height: 200px;
    background: linear-gradient(170deg, #cfd8e1 0%, #a88a64 55%, #5b6b7c 100%); }

  .label { font-family: var(--head); font-weight: 700; text-transform: uppercase; letter-spacing: .3px; }
  .copy { font-size: 6.3px; line-height: 1.5; }

  /* outside spread */
  .what-we-do { left: 10px; top: 14px; width: 190px; color: #d9dde1; }
  .what-we-do .label, .lets-talk .label { color: var(--blue-bright); font-size: 9.5px; margin-bottom: 4px; }
  .lets-talk { left: 10px; top: 146px; width: 190px; color: #d9dde1; }
  .tick-list { list-style: none; margin-top: 5px; }
  .tick-list li { display: flex; align-items: center; gap: 5px; font-size: 7.5px; font-weight: 700; color: #fff; margin-bottom: 5px; }
  .tick { width: 9px; height: 9px; flex: none; }

  .contact { left: 232px; top: 76px; width: 180px; color: var(--ink); }
  .contact .label { font-size: 13px; margin-bottom: 8px; }
  .contact-line { display: flex; align-items: center; gap: 6px; font-size: 7.5px; margin-bottom: 6px; }
  .contact-line svg { width: 9px; height: 9px; flex: none; }

  .tagline { left: 211px; top: 288px; width: 211px; text-align: center; font-family: var(--head); text-transform: uppercase; }
  .tagline-small { font-size: 9px; color: var(--ink); letter-spacing: .4px; }
  .tagline-big { font-size: 15.5px; color: var(--blue); letter-spacing: .6px; }

  .brand { display: flex; align-items: center; justify-content: center; gap: 5px; }
  .brand-mark { width: 14px; height: 14px; background: var(--blue); }
  .brand-name { font-family: var(--head); font-weight: 700; color: var(--ink); }
  .brand--middle { left: 211px; top: 376px; width: 211px; }
  .brand--middle .brand-name { font-size: 24px; color: var(--blue-deep); }
  .brand--right { left: 422px; top: 42px; width: 210px; }
  .brand--right .brand-name { font-size: 26px; }
  .brand--inside { left: 211px; top: 160px; width: 211px; }
  .brand--inside .brand-name { font-size: 22px; }

  .web-bar { height: 22px; border-radius: 5px; color: #fff; font-size: 7.5px; font-weight: 600;
    display: flex; align-items: center; justify-content: center; }
  .web-bar--blue { left: 226px; top: 460px; width: 182px; background: var(--blue); }
  .web-bar--dark { left: 436px; top: 460px; width: 182px; background: var(--ink-deep); }

  .expert { left: 436px; top: 360px; width: 190px; color: #fff; font-family: var(--head); text-transform: uppercase; line-height: 1.2; }
  .expert-big { font-size: 18px; font-weight: 700; letter-spacing: .5px; }
  .expert-small { font-size: 10.5px; letter-spacing: .3px; }

  /* inside spread */
  .services { left: 12px; top: 20px; width: 188px; color: var(--grey-text); }
  .services .label { color: var(--ink); font-size: 11px; margin-bottom: 6px; }
  .service-title { font-size: 7px; font-weight: 700; color: var(--blue); text-transform: uppercase; line-height: 1.3; margin-top: 7px; }
  .services .copy { margin-top: 2px; }

  .headline { left: 250px; top: 22px; width: 250px; text-align: center; font-family: var(--head); font-weight: 700; text-transform: uppercase; color: var(--ink); line-height: 1.25; }
  .headline-lead { font-size: 12.5px; }
  .headline-mid { font-size: 12.5px; }
  .headline-mid em { font-style: normal; color: #fff; font-size: 16px; }
  .headline-tail { font-size: 10px; }

  .offerings { left: 224px; top: 218px; width: 188px; color: #cfd4d9; }
  .offer-title { font-size: 7px; font-weight: 700; color: var(--blue-bright); text-transform: uppercase; margin-top: 8px; margin-bottom: 2px; }
  .offerings .offer-title:first-child { margin-top: 0; }
  .bullet-list { list-style: none; }
  .bullet-list li { font-size: 6.8px; color: #fff; display: flex; align-items: center; gap: 5px; margin-bottom: 3px; }
  .bullet-list li::before { content: ""; width: 4px; height: 4px; background: var(--blue-bright); flex: none; }

  .outsource { left: 436px; top: 196px; width: 186px; color: #fff; }
  .outsource .label { font-size: 10px; line-height: 1.2; }
  .benefit-grid { list-style: none; display: grid; grid-template-columns: 1fr 1fr; gap: 4px 6px; margin-top: 8px; }
  .benefit-grid li { display: flex; align-items: center; gap: 4px; font-size: 6.8px; font-weight: 700; }
  .process { left: 436px; top: 296px; width: 186px; color: #fff; }
  .process .label { font-size: 10px; margin-bottom: 6px; }
  .process-list { list-style: none; }
  .process-list li { display: flex; gap: 5px; font-size: 6.5px; line-height: 1.35; margin-bottom: 5px; font-weight: 600; }
  .process-list .tick { margin-top: 1px; }
  .footer-bar { left: 436px; top: 462px; width: 182px; height: 20px; border-radius: 5px; background: var(--ink-deep); }
</style>
</head>
<body>

<!-- Outside spread -->
<section class="brochure brochure--outside" aria-label="Brochure outside spread">
  <div class="photo photo--desk" role="img" aria-label="Photo of a desk with financial charts, eyeglasses and a calculator"></div>
  <div class="photo photo--team" role="img" aria-label="Photo of two smiling professionals working together at a computer"></div>

  <svg class="panel-art" viewBox="0 0 632 490" aria-hidden="true">
    <defs>
      <linearGradient id="middleGlow" x1="0" y1="0" x2="0" y2="1">
        <stop offset="0" stop-color="#ffffff"/>
        <stop offset="1" stop-color="#e3e7eb"/>
      </linearGradient>
      <linearGradient id="blueFade" x1="0" y1="0" x2="0" y2="1">
        <stop offset="0" stop-color="#2a9be2"/>
        <stop offset="1" stop-color="#136aa8"/>
      </linearGradient>
    </defs>
    <rect x="211" y="0" width="211" height="490" fill="url(#middleGlow)"/>
    <path d="M0,0 H211 V238 C140,250 70,258 0,266 Z" fill="#28292c"/>
    <path d="M211,214 C290,200 360,180 422,165 L422,192 C350,208 290,224 211,238 Z" fill="#28292c"/>
    <path d="M0,266 C70,258 140,250 211,238 C290,224 350,208 422,192 C440,188 455,186 470,186 L470,194 C455,196 440,200 422,206 C350,222 290,238 211,252 C140,264 70,272 0,282 Z" fill="#1f8fd8"/>
    <path d="M0,286 C70,276 140,268 211,256 C290,242 350,226 422,210" fill="none" stroke="#ffffff" stroke-width="1.5"/>
    <path d="M422,0 H632 V108 C560,118 480,138 422,165 Z" fill="#eef1f4"/>
    <path d="M422,158 C480,132 560,114 632,104" fill="none" stroke="#1f8fd8" stroke-width="3"/>
    <path d="M460,0 C520,30 580,40 632,38 V0 Z" fill="#d7e8f5"/>
    <path d="M422,352 C500,346 570,330 632,300 V490 H422 Z" fill="url(#blueFade)"/>
    <path d="M422,344 C500,338 570,322 632,292" fill="none" stroke="#28292c" stroke-width="5"/>
    <rect x="0" y="470" width="211" height="20" fill="#28292c"/>
  </svg>

  <div class="what-we-do">
    <h3 class="label">What we do</h3>
    <p class="copy">We let owners spend more time on their core business by providing full bookkeeping and consulting services. We deliver the financial data and tools that help a business grow profit and focus on the areas that matter most. Think of us as an extension of your team.</p>
  </div>

  <div class="lets-talk">
    <h3 class="label">Let's talk</h3>
    <p class="copy">Schedule a no-obligation consultation today</p>
    <ul class="tick-list">
      <li><svg class="tick" viewBox="0 0 10 10"><path d="M1.5,5.2 L4,7.6 L8.6,2.4" fill="none" stroke="#35a9ec" stroke-width="1.8"/></svg>Trustworthy</li>
      <li><svg class="tick" viewBox="0 0 10 10"><path d="M1.5,5.2 L4,7.6 L8.6,2.4" fill="none" stroke="#35a9ec" stroke-width="1.8"/></svg>Experienced</li>
      <li><svg class="tick" viewBox="0 0 10 10"><path d="M1.5,5.2 L4,7.6 L8.6,2.4" fill="none" stroke="#35a9ec" stroke-width="1.8"/></svg>Reliable</li>
    </ul>
  </div>

  <div class="contact">
    <h3 class="label">Contact us</h3>
    <p class="contact-line">
      <svg viewBox="0 0 10 10" aria-hidden="true"><path d="M2.2,1 L3.8,1 L4.5,3.2 L3.4,4.1 C4,5.4 4.7,6.1 5.9,6.6 L6.8,5.5 L9,6.2 L9,7.8 C9,8.5 8.4,9 7.7,9 C4.2,8.6 1.4,5.8 1,2.3 C1,1.6 1.5,1 2.2,1 Z" fill="#1f8fd8"/></svg>
      555.014.2290
    </p>
    <p class="contact-line">
      <svg viewBox="0 0 10 10" aria-hidden="true"><rect x="0.8" y="2" width="8.4" height="6" rx="0.8" fill="#1f8fd8"/><path d="M1.2,2.6 L5,5.4 L8.8,2.6" fill="none" stroke="#fff" stroke-width="0.8"/></svg>
      mara@halvorineledgers.com
    </p>
  </div>

  <div class="tagline">
    <p class="tagline-small">It's not just my business</p>
    <p class="tagline-big">It's my name</p>
  </div>

  <div class="brand brand--middle"><span class="brand-mark"></span><span class="brand-name">HL&amp;A</span></div>
  <div class="brand brand--right"><span class="brand-mark"></span><span class="brand-name">HL&amp;A</span></div>

  <div class="expert">
    <p class="expert-big">Expert</p>
    <p class="expert-small">Bookkeeping services</p>
    <p class="expert-small">for small business</p>
  </div>

  <p class="web-bar web-bar--blue">www.halvorineledgers.com</p>
  <p class="web-bar web-bar--dark">www.halvorineledgers.com</p>
</section>

<!-- Inside spread -->
<section class="brochure brochure--inside" aria-label="Brochure inside spread">
  <div class="photo photo--growth" role="img" aria-label="Photo of a hand raising a glowing figure among a network of business people icons"></div>
  <div class="photo photo--coins" role="img" aria-label="Photo of stacked coins, a calculator and a pen on financial papers"></div>

  <svg class="panel-art" viewBox="0 0 632 490" aria-hidden="true">
    <defs>
      <linearGradient id="blueDrop" x1="0" y1="0" x2="0" y2="1">
        <stop offset="0" stop-color="#2a9be2"/>
        <stop offset="1" stop-color="#1677bd"/>
      </linearGradient>
    </defs>
    <path d="M0,0 H211 V305 C150,298 70,310 0,330 Z" fill="#ffffff"/>
    <path d="M0,330 C70,310 150,298 211,305 L211,318 C150,312 70,322 0,344 Z" fill="#28292c"/>
    <path d="M211,142 C300,165 370,170 422,170 L422,205 C360,200 280,205 211,215 Z" fill="#ffffff"/>
    <path d="M211,215 C280,205 360,200 422,205 V490 H211 Z" fill="#28292c"/>
    <path d="M211,455 C280,472 350,472 422,450 V490 H211 Z" fill="#1f8fd8"/>
    <path d="M422,170 C500,165 570,142 632,124 V490 H422 Z" fill="url(#blueDrop)"/>
    <path d="M211,118 C300,142 370,146 422,145 C500,142 570,120 632,100 L632,124 C570,142 500,165 422,170 C370,170 300,165 211,142 Z" fill="#28292c"/>
    <path d="M211,112 C300,136 370,140 422,139 C500,136 570,114 632,94" fill="none" stroke="#35a9ec" stroke-width="2"/>
  </svg>

  <div class="services">
    <h3 class="label">Our services</h3>
    <h4 class="service-title">Full charge bookkeeping</h4>
    <p class="copy">We can manage all aspects of your bookkeeping and business financials and communicate with you as often as you want.</p>
    <h4 class="service-title">Cash management/bill pay (invoicing) &amp; vendor management</h4>
    <p class="copy">We can handle every step from receiving bills, talking with vendors and paying bills, to using early payment discounts.</p>
    <h4 class="service-title">Financial statements</h4>
    <p class="copy">Profit and Loss – Balance Sheet – Statement of Cash Flow – Industry Specific</p>
    <p class="copy">We accurately prepare monthly, quarterly &amp; annual financial statements on time. We review them with you so you understand the financial health of your business.</p>
  </div>

  <div class="headline">
    <p class="headline-lead">The financial numbers</p>
    <p class="headline-mid">are <em>the heart beat</em></p>
    <p class="headline-tail">of an organization</p>
  </div>

  <div class="brand brand--inside"><span class="brand-mark"></span><span class="brand-name">HL&amp;A</span></div>

  <div class="offerings">
    <h4 class="offer-title">Account reconciliations</h4>
    <p class="copy">From bank accounts to credit card statements to vendor statements. We reconcile every account that affects your finances.</p>
    <h4 class="offer-title">Professional liaison</h4>
    <p class="copy">We work directly with your other business partners: bankers, CPA, insurance, payroll, attorneys. Need a loan? We work with your banker to keep it simple. Let us handle that while you serve your customers.</p>
    <h4 class="offer-title">Business services</h4>
    <ul class="bullet-list">
      <li>Budget</li>
      <li>Create Proper Financial Systems</li>
      <li>Projections</li>
    </ul>
  </div>

  <div class="outsource">
    <h3 class="label">Why outsource<br>bookkeeping?</h3>
    <ul class="benefit-grid">
      <li><svg class="tick" viewBox="0 0 10 10"><path d="M1.5,5.2 L4,7.6 L8.6,2.4" fill="none" stroke="#ffffff" stroke-width="1.8"/></svg>SAVE TIME</li>
      <li><svg class="tick" viewBox="0 0 10 10"><path d="M1.5,5.2 L4,7.6 L8.6,2.4" fill="none" stroke="#ffffff" stroke-width="1.8"/></svg>FOCUSED STAFF</li>
      <li><svg class="tick" viewBox="0 0 10 10"><path d="M1.5,5.2 L4,7.6 L8.6,2.4" fill="none" stroke="#ffffff" stroke-width="1.8"/></svg>SAVE MONEY</li>
      <li><svg class="tick" viewBox="0 0 10 10"><path d="M1.5,5.2 L4,7.6 L8.6,2.4" fill="none" stroke="#ffffff" stroke-width="1.8"/></svg>TECHNOLOGY</li>
      <li><svg class="tick" viewBox="0 0 10 10"><path d="M1.5,5.2 L4,7.6 L8.6,2.4" fill="none" stroke="#ffffff" stroke-width="1.8"/></svg>EXPERTISE</li>
      <li><svg class="tick" viewBox="0 0 10 10"><path d="M1.5,5.2 L4,7.6 L8.6,2.4" fill="none" stroke="#ffffff" stroke-width="1.8"/></svg>EXPERIENCE</li>
    </ul>
  </div>

  <div class="process">
    <h3 class="label">The process</h3>
    <ul class="process-list">
      <li><svg class="tick" viewBox="0 0 10 10"><path d="M1.5,5.2 L4,7.6 L8.6,2.4" fill="none" stroke="#ffffff" stroke-width="1.8"/></svg>Contact Us – we'd like to hear from you</li>
      <li><svg class="tick" viewBox="0 0 10 10"><path d="M1.5,5.2 L4,7.6 L8.6,2.4" fill="none" stroke="#ffffff" stroke-width="1.8"/></svg>No-Obligation Consultation</li>
      <li><svg class="tick" viewBox="0 0 10 10"><path d="M1.5,5.2 L4,7.6 L8.6,2.4" fill="none" stroke="#ffffff" stroke-width="1.8"/></svg>Review Current Process – Identify strengths and weaknesses</li>
      <li><svg class="tick" viewBox="0 0 10 10"><path d="M1.5,5.2 L4,7.6 L8.6,2.4" fill="none" stroke="#ffffff" stroke-width="1.8"/></svg>Recommend and implement new bookkeeping process</li>
      <li><svg class="tick" viewBox="0 0 10 10"><path d="M1.5,5.2 L4,7.6 L8.6,2.4" fill="none" stroke="#ffffff" stroke-width="1.8"/></svg>Ongoing bookkeeping partnership</li>
      <li><svg class="tick" viewBox="0 0 10 10"><path d="M1.5,5.2 L4,7.6 L8.6,2.4" fill="none" stroke="#ffffff" stroke-width="1.8"/></svg>Provide your company with more value and service to keep running your business (ongoing)</li>
    </ul>
  </div>

  <div class="footer-bar"></div>
</section>

</body>
</html>
```